professional business card

A Clean looking business card for a money transfer company. Our company is call Velorix= Transfer + Send = Transcend (next level)
to show professionalism as well as some effects to show digital tech.

1 side to have position, name and address
2 side to have company name and show that we provide money exchange and cross-border money transfer

Target Market(s)

Remittance companies and high net worth individuals

Industry/Entity Type

Finance

Contact Information for Business Card

Name, address, email, title, services- money exchange and cross-border remittance

Requirements
Nice to have
• Digital age feel

```html
<!DOCTYPE html>
<html lang="en">
<head>
<meta charset="utf-8">
<title>Velorix Business Card</title>
<link href="https://fonts.googleapis.com/css2?family=Montserrat:wght@400;500;600;700&display=swap" rel="stylesheet">
<style>
  :root {
    --backdrop: #bfe6f3;
    --ink: #263642;
    --accent: #6ccbdc;
    --paper: #ffffff;
    --pattern: #d6eef6;
    --body-text: #2c3a44;
  }
  * { margin: 0; padding: 0; box-sizing: border-box; }
  html, body {
    width: 1046px;
    height: 1200px;
    overflow: hidden;
  }
  body {
    background: var(--backdrop);
    font-family: "Montserrat", sans-serif;
    position: relative;
  }
  .card {
    position: absolute;
    left: 183px;
    width: 680px;
    height: 416px;
  }
  .card--front {
    top: 200px;
    background: var(--ink);
  }
  .card--back {
    top: 690px;
    background: var(--paper);
  }
  .front-wordmark {
    position: absolute;
    top: 150px;
    left: 0;
    width: 100%;
    text-align: center;
    font-size: 52px;
    font-weight: 700;
    letter-spacing: 4px;
    color: var(--accent);
  }
  .services {
    position: absolute;
    top: 362px;
    left: 0;
    width: 100%;
    text-align: center;
    font-size: 14px;
    font-weight: 400;
    color: var(--paper);
    letter-spacing: 0.2px;
  }
  .brand {
    position: absolute;
    top: 54px;
    left: 45px;
    display: flex;
    align-items: center;
    gap: 12px;
  }
  .brand-square {
    width: 26px;
    height: 26px;
    background: var(--accent);
  }
  .brand-name {
    font-size: 32px;
    font-weight: 600;
    color: var(--ink);
    letter-spacing: 0.5px;
  }
  .person {
    position: absolute;
    top: 226px;
    left: 45px;
  }
  .person-name {
    font-size: 19px;
    font-weight: 600;
    color: var(--ink);
    letter-spacing: 0.4px;
  }
  .person-title {
    font-size: 17px;
    font-weight: 500;
    color: var(--accent);
    margin-top: 4px;
  }
  .contact {
    position: absolute;
    top: 228px;
    left: 317px;
    font-size: 17px;
    color: var(--body-text);
    line-height: 26px;
  }
  .website {
    position: absolute;
    top: 356px;
    left: 317px;
    font-size: 17px;
    color: var(--body-text);
  }
  .pattern-strip {
    position: absolute;
    top: 0;
    right: 28px;
    width: 50px;
    height: 100%;
    background: var(--pattern);
  }
</style>
</head>
<body>
  <section class="card card--front">
    <div class="front-wordmark">VELORIX</div>
    <p class="services">SERVICES- MONEY EXCHANGE &amp; CROSS-BORDER REMITTANCE</p>
  </section>

  <section class="card card--back">
    <div class="brand">
      <span class="brand-square"></span>
      <span class="brand-name">VELORIX</span>
    </div>
    <div class="person">
      <p class="person-name">DANIEL REYES</p>
      <p class="person-title">CEO</p>
    </div>
    <div class="contact">
      <p>+55 21 95555-0123</p>
      <p>danielreyes@velorix.com</p>
    </div>
    <p class="website">www.velorix.com</p>
    <div class="pattern-strip" role="img" aria-label="Faint vertical band of repeating interlocking brand pattern"></div>
  </section>
</body>
</html>
```